MOBILE DOG GROOMING BUSINESS CARD

We need a business card for a new local Mobile Dog groomer wanting to attract new business.

Our logo must be incorporated on the first page with contact details on the front or back of the card. We were thinking for the back of the card it could have the " your next appointment is on date...time...

Target Market(s)

local pet lovers and owners

Industry/Entity Type

Business

Contact Information for Business Card

Maren Tolley
Certified Professional Groomer
0437825190
www.pawluxemobilewash.com.au
pawluxemobilewash@quillmail.com

Font styles to use
Script

Colors

Designer to choose colors to be used in the design.

Requirements
Must have
• Must have our logo on the front
Possibly something that says like our page and check us out on facebook
Nice to have
• Colours are something we would like - matched in with the logo.
Should not have
• Clutter

```html
<!DOCTYPE html>
<html lang="en">
<head>
<meta charset="utf-8">
<title>Paw Luxe Mobile Wash – Next Appointment Card</title>
<link rel="stylesheet" href="https://fonts.googleapis.com/css2?family=Raleway:wght@200;300;400&display=swap">
<style>
  :root {
    --paper: #ffffff;
    --brand-crimson: #c4304f;
    --brand-teal: #2f86a8;
    --rose: #d06a8c;
    --grey-text: #8c8c8c;
    --light-grey: #a6a6a6;
    --navy: #1f1f4a;
    --silhouette: #111111;
  }
  html, body {
    margin: 0;
    padding: 0;
    overflow: hidden;
    background: var(--paper);
  }
  .card {
    position: relative;
    width: 1200px;
    height: 718px;
    background: var(--paper);
    overflow: hidden;
    font-family: "Raleway", sans-serif;
  }
  .brand-mark {
    position: absolute;
    left: 168px;
    top: 20px;
    width: 320px;
    height: 320px;
  }
  .brand-name {
    position: absolute;
    left: 70px;
    top: 352px;
    width: 520px;
    text-align: center;
    margin: 0;
    font-size: 48px;
    font-weight: 300;
    color: var(--brand-crimson);
    white-space: nowrap;
  }
  .dog-silhouette {
    position: absolute;
    left: 978px;
    top: 28px;
    width: 190px;
    height: 228px;
  }
  .appointment-title {
    position: absolute;
    left: 589px;
    top: 396px;
    margin: 0;
    font-size: 60px;
    font-weight: 200;
    color: var(--grey-text);
    white-space: nowrap;
  }
  .field {
    position: absolute;
    left: 28px;
    width: 1084px;
    height: 72px;
  }
  .field-date { top: 468px; }
  .field-time { top: 542px; }
  .field-label {
    position: absolute;
    left: 0;
    bottom: 0;
    font-size: 60px;
    font-weight: 300;
    color: var(--rose);
    line-height: 1;
  }
  .field-line {
    position: absolute;
    left: 170px;
    right: 0;
    bottom: 10px;
    height: 4px;
    background: var(--rose);
  }
  .contact {
    position: absolute;
    left: 0;
    width: 1070px;
    margin: 0;
    text-align: center;
    white-space: nowrap;
    font-size: 30px;
  }
  .contact-web {
    top: 620px;
    color: var(--light-grey);
    letter-spacing: 6px;
    font-weight: 300;
  }
  .contact-email {
    top: 656px;
    color: var(--navy);
    letter-spacing: 3.5px;
    font-weight: 400;
  }
</style>
</head>
<body>
  <main class="card">
    <svg class="brand-mark" viewBox="0 0 320 320" aria-hidden="true">
      <circle cx="160" cy="160" r="158" fill="var(--brand-teal)"/>
    </svg>
    <h1 class="brand-name">Paw Luxe Mobile Wash</h1>

    <svg class="dog-silhouette" viewBox="0 0 190 228" role="img" aria-label="Silhouette of a small terrier sitting">
      <rect x="0" y="0" width="190" height="228" rx="40" fill="var(--silhouette)"/>
    </svg>

    <h2 class="appointment-title">Next Appointment</h2>

    <div class="field field-date">
      <span class="field-label">Date</span>
      <span class="field-line"></span>
    </div>
    <div class="field field-time">
      <span class="field-label">Time</span>
      <span class="field-line"></span>
    </div>

    <p class="contact contact-web">www.pawluxemobilewash.com.au</p>
    <p class="contact contact-email">pawluxemobilewash@quillmail.com</p>
  </main>
</body>
</html>
```